Personal Business Card Design Project

I am looking for a business card to be able to hand to both Chinese and Australian businessman.
I am a self employed consultant and just need my name, phone number and email address on the card. No Business Name and No Website.
I want it to look like an exclusive prestigious card.
I would like the background to be be a glossy red and the writing to be gold. (This applies to both sides of the card).
It must have English on one side and Chinese (Mandarin) on the reverse.
Details you will require
Name : Wade Emmerson
Phone : + 61 493 207 158
Email : wadeyemmerson@brightpost.example
Thank you everybody for your designs.
Industry/Entity Type
Business

```html
<!DOCTYPE html>
<html lang="en">
<head>
<meta charset="utf-8">
<title>Wade Emmerson – Business Card</title>
<link href="https://fonts.googleapis.com/css2?family=Jost:wght@400;500&display=swap" rel="stylesheet">
<style>
  :root {
    --backdrop: #0b0b0b;
    --card-red-light: #b81c24;
    --card-red: #8e1419;
    --card-red-dark: #4a0a0d;
    --medallion-red: #d01e27;
    --medallion-red-deep: #b4161e;
    --medallion-ring: #c8782f;
    --gold: #f2c23a;
    --gold-shadow: rgba(60, 10, 5, 0.6);
  }
  html, body {
    margin: 0;
    padding: 0;
    width: 1200px;
    height: 960px;
    overflow: hidden;
    background: var(--backdrop);
  }
  .canvas {
    position: relative;
    width: 1200px;
    height: 960px;
  }
  .business-card {
    position: absolute;
    left: 75px;
    top: 170px;
    width: 1050px;
    height: 620px;
    border: 2px solid #f4f4f4;
    box-sizing: border-box;
    background: radial-gradient(ellipse at 50% 40%, var(--card-red-light) 0%, var(--card-red) 55%, var(--card-red-dark) 100%);
    overflow: hidden;
  }
  .medallion {
    position: absolute;
    left: 50%;
    top: 50%;
    width: 500px;
    height: 500px;
    margin: -250px 0 0 -250px;
    border-radius: 50%;
    box-sizing: border-box;
    border: 9px solid var(--medallion-ring);
    background: radial-gradient(circle at 50% 35%, var(--medallion-red) 0%, var(--medallion-red-deep) 100%);
    box-shadow: 0 0 30px rgba(40, 0, 0, 0.45);
    display: flex;
    flex-direction: column;
    align-items: center;
    justify-content: center;
    font-family: "Jost", "Futura", sans-serif;
    color: var(--gold);
    text-align: center;
  }
  .holder-name {
    margin: 0 0 14px;
    font-size: 44px;
    font-weight: 500;
    letter-spacing: 1px;
    text-transform: uppercase;
    text-shadow: 2px 3px 3px var(--gold-shadow);
  }
  .contact-icon {
    display: block;
    width: 46px;
    height: 34px;
    fill: var(--gold);
  }
  .contact-line {
    margin: 6px 0 12px;
    font-size: 27px;
    font-weight: 400;
    letter-spacing: 1px;
  }
  .contact-line.email {
    font-size: 24px;
    letter-spacing: 0.3px;
    margin-bottom: 0;
  }
</style>
</head>
<body>
<main class="canvas">
  <section class="business-card">
    <div class="medallion">
      <h1 class="holder-name">Wade Emmerson</h1>

      <svg class="contact-icon" viewBox="0 0 46 34" aria-hidden="true">
        <path d="M3 11 C3 4 43 4 43 11 L43 14 L33 14 L33 10 C28 8 18 8 13 10 L13 14 L3 14 Z"/>
        <path d="M12 16 L34 16 L40 32 L6 32 Z"/>
        <circle cx="23" cy="24" r="5" fill="var(--medallion-red)"/>
        <circle cx="23" cy="24" r="2"/>
      </svg>
      <p class="contact-line phone">+ 61 493 207 158</p>

      <svg class="contact-icon" viewBox="0 0 46 34" aria-hidden="true">
        <rect x="4" y="4" width="38" height="26" fill="none" stroke="var(--gold)" stroke-width="2.5"/>
        <path d="M4 4 L23 20 L42 4" fill="none" stroke="var(--gold)" stroke-width="2.5"/>
        <path d="M4 30 L18 16 M42 30 L28 16" fill="none" stroke="var(--gold)" stroke-width="2"/>
      </svg>
      <p class="contact-line email">wadeyemmerson@brightpost.example</p>
    </div>
  </section>
</main>
</body>
</html>
```